Web Design Project for Communications Agency

The design I need (PSD file) is for an agency offering specialised PR and communications services for customers in the healthcare sector.

OBJECTIVES OF THE WEBSITE:
1. To promote the agency's communication services
2. To position Solène Verbruggen as an industry leader, an expert in healthcare PR and communications by highlighting blogposts and social media.

WHAT I NEED:
1st, I need the design for the Home Page ONLY.
Once approved, I will need the other pages designed as well. (Here is prototype that we've already developed for the Website that will guide you in the design:
http://qoravenlab.com/solenverbruggen/)

VISUAL INSPIRATION
We want to give this Website a "Flat Design" look. Here are some websites for inspiration :
- http://lumbrafolk.com/#!/process
- http://www.quillmarsh.co/
- http://dorvellink.com/

Also, reuse images found on the company's current Website :
http://www.solenverbruggen.com/fr/index.html

HOMEPAGE MAIN ELEMENTS:
1. Main menu : 6 sections
Accueil | Agence | Services | Approche | Publications | Contact

2. Main Call To Action (big dark rectangle in prototype):
Can be slider or just an information bloc.

3. Publications récentes :
The 4 latest blog posts must be features on the homepage (will be linked with the "Publications" section)

4. Dynamic Footer :
Contains a Chirpline feed and a Subscribe to our Newsletter feature (revecez nos publications)

OTHER PAGES (to design once Homepage is approved)
- Agence (about us)
- Services (our team)
- Approche (our approach)
- Publications (blog articles)
- Contact (Contact us)

• Please refer to prototype :
http://qoravenlab.com/solenverbruggen/
Must have ALL features present in prototype.

Also, must reuse this picture in the design : http://solenverbruggen.com/static/images/home-big-box.jpg

Finally, you will find attached the company logo.

```html
<!DOCTYPE html>
<html lang="fr">
<head>
<meta charset="utf-8">
<title>Solène Verbruggen – Gestion d'enjeux, affaires publiques</title>
<link rel="stylesheet" href="https://fonts.googleapis.com/css2?family=Open+Sans:wght@300;400;600;700&family=Cabin:wght@400;600&display=swap">
<style>
  :root {
    --red: #e2453c;
    --red-dark: #b8302a;
    --yellow: #f7d21a;
    --ink: #333333;
    --muted: #6b6b6b;
    --card-light: #e9e9e9;
    --card-dark: #3b3b3b;
    --footer: #2d2d2d;
    --footer-deep: #232323;
    --page: #ffffff;
  }
  * { box-sizing: border-box; margin: 0; padding: 0; }
  html, body { width: 1200px; height: 2432px; overflow: hidden; }
  body { position: relative; background: var(--page); font-family: "Open Sans", sans-serif; color: var(--ink); }

  /* Header */
  .site-header { position: absolute; left: 0; top: 0; width: 1200px; height: 176px; }
  .brand-name { position: absolute; left: 32px; top: 18px; color: var(--red); font-family: "Cabin", sans-serif; font-weight: 600; font-size: 44px; line-height: 46px; }
  .social { position: absolute; right: 60px; top: 16px; display: flex; gap: 14px; }
  .social span { width: 34px; height: 34px; border-radius: 50%; background: #4a4a4a; display: block; }
  .utility { position: absolute; right: 60px; top: 74px; font-size: 14px; color: var(--muted); }
  .main-nav { position: absolute; left: 0; top: 132px; width: 1200px; height: 44px; background: var(--yellow); }
  .tagline { position: absolute; left: 32px; top: 4px; font-size: 13px; font-weight: 700; line-height: 17px; color: var(--red-dark); letter-spacing: .5px; }
  .main-nav ul { position: absolute; left: 380px; top: 0; display: flex; list-style: none; }
  .main-nav li { padding: 0 26px; line-height: 44px; font-size: 14px; font-weight: 600; color: var(--ink); }
  .main-nav li.active { color: var(--red); border-top: 4px solid var(--red); line-height: 36px; }

  /* Hero */
  .hero { position: absolute; left: 0; top: 176px; width: 1200px; height: 356px; background: linear-gradient(90deg, #f2f2f2 0%, #e4e4e4 60%, #d9d9d9 100%); }
  .hero-visual { position: absolute; left: 0; top: 0; width: 760px; height: 356px; background: linear-gradient(120deg, #fbfbfb 0%, #e8e8e8 55%, #cfcfcf 100%); }
  .hero-copy { position: absolute; left: 800px; top: 90px; width: 370px; font-family: "Cabin", sans-serif; font-size: 26px; line-height: 34px; color: #3a3a3a; }
  .btn-primary { position: absolute; left: 820px; top: 264px; width: 340px; height: 64px; background: var(--red); color: #fff; font-family: "Cabin", sans-serif; font-size: 28px; line-height: 64px; text-align: center; }

  /* Publications */
  .section-head { position: absolute; left: 140px; top: 560px; width: 920px; height: 48px; border-bottom: 1px solid #d5d5d5; }
  .section-head h2 { font-weight: 300; font-size: 30px; color: #555; }
  .btn-all { position: absolute; right: 0; top: 8px; background: #2b2b2b; color: #fff; font-size: 12px; font-weight: 600; padding: 6px 14px; }

  .post { position: absolute; left: 140px; width: 920px; height: 320px; background: var(--card-light); }
  .post.featured { background: var(--card-dark); }
  .post-image { position: absolute; left: 20px; top: 24px; width: 440px; height: 272px; }
  .post-body { position: absolute; left: 480px; top: 20px; width: 420px; }
  .post-title { color: var(--red); font-family: "Cabin", sans-serif; font-size: 26px; font-weight: 400; }
  .post-date { color: var(--red); font-size: 12px; margin: 2px 0 10px; }
  .post-text { font-size: 11.5px; line-height: 16px; color: #555; margin-bottom: 8px; }
  .featured .post-text { color: #e6e6e6; }
  .btn-read { position: absolute; right: 20px; bottom: 20px; height: 40px; background: var(--yellow); color: var(--ink); font-size: 17px; font-weight: 600; line-height: 40px; padding: 0 10px 0 18px; display: flex; align-items: center; gap: 10px; }

  /* Footer */
  .site-footer { position: absolute; left: 0; top: 2112px; width: 1200px; height: 320px; background: var(--footer); color: #ddd; }
  .feed-name { position: absolute; left: 140px; top: 22px; font-family: "Cabin", sans-serif; font-size: 40px; font-weight: 600; color: #3fb4e5; }
  .tweets { position: absolute; left: 140px; top: 100px; width: 420px; list-style: none; }
  .tweets li { position: relative; padding-left: 30px; font-size: 11.5px; line-height: 16px; margin-bottom: 16px; color: #ccc; }
  .tweets li::before { content: ""; position: absolute; left: 0; top: 4px; border-left: 14px solid var(--yellow); border-top: 5px solid transparent; border-bottom: 5px solid transparent; }
  .tweets .handle { color: #8ecde9; }
  .btn-follow { position: absolute; left: 140px; top: 248px; background: var(--yellow); color: var(--ink); font-size: 15px; font-weight: 600; padding: 8px 16px; }
  .newsletter { position: absolute; left: 640px; top: 22px; width: 440px; }
  .newsletter h3 { font-family: "Cabin", sans-serif; font-weight: 400; font-size: 30px; color: #fff; margin-bottom: 28px; }
  .field { display: flex; align-items: center; margin-bottom: 16px; }
  .field label { width: 140px; font-size: 15px; color: #fff; }
  .field span { width: 280px; height: 30px; background: #3c3c3c; display: block; }
  .btn-subscribe { margin-left: 140px; width: 180px; height: 42px; background: #e26a64; color: #fff; font-size: 17px; line-height: 42px; text-align: center; }
  .legal { position: absolute; left: 0; bottom: 0; width: 1200px; height: 40px; background: var(--footer-deep); font-size: 11px; line-height: 40px; color: #888; padding-left: 140px; }
</style>
</head>
<body>

<header class="site-header">
  <div class="brand-name">Solène<br>Verbruggen</div>
  <div class="social" aria-label="Réseaux sociaux"><span></span><span></span><span></span></div>
  <div class="utility">Login | English</div>
  <nav class="main-nav">
    <div class="tagline">GESTION D'ENJEUX<br>AFFAIRES PUBLIQUES</div>
    <ul>
      <li class="active">ACCUEIL</li>
      <li>AGENCE</li>
      <li>SERVICES</li>
      <li>APPROCHE</li>
      <li>PUBLICATIONS</li>
      <li>CONTACT</li>
    </ul>
  </nav>
</header>

<section class="hero">
  <div class="hero-visual" role="img" aria-label="Photo d'un consultant pointant un réseau de personnes reliées"></div>
  <p class="hero-copy">Cabinet-conseil en communications et affaires publiques spécialisé dans le secteur de la santé.</p>
  <div class="btn-primary">En Savoir Plus</div>
</section>

<div class="section-head">
  <h2>Publication récentes</h2>
  <span class="btn-all">View All</span>
</div>

<article class="post featured" style="top:640px">
  <div class="post-image" role="img" aria-label="Photo d'une coccinelle sur une feuille" style="background:linear-gradient(135deg,#cfe6a0,#7fb34a 60%,#4c7d2c)"></div>
  <div class="post-body">
    <h3 class="post-title">Titre de la publication</h3>
    <p class="post-date">23 juillet 2013</p>
    <p class="post-text">Ce court billet présente un aperçu des enjeux actuels en communication santé. Nous y abordons les relations avec les médias, la gestion des parties prenantes et les stratégies d'affaires publiques qui soutiennent les organisations du réseau de la santé au quotidien.</p>
    <p class="post-text">Découvrez nos recommandations pratiques, des exemples concrets tirés de nos mandats récents et quelques pistes de réflexion pour mieux planifier vos prochaines prises de parole publiques.</p>
  </div>
  <div class="btn-read">Article complet <svg width="22" height="22" viewBox="0 0 22 22"><rect width="22" height="22" fill="#333"/><path d="M8 5l6 6-6 6" stroke="#f7d21a" stroke-width="3" fill="none"/></svg></div>
</article>

<article class="post" style="top:960px">
  <div class="post-image" role="img" aria-label="Photo d'un papillon sur des fleurs jaunes" style="background:linear-gradient(160deg,#bfe3f5,#7fc4e8 45%,#f2c53a 75%,#e59a1e)"></div>
  <div class="post-body">
    <h3 class="post-title">Titre de la publication</h3>
    <p class="post-date">23 juillet 2013</p>
    <p class="post-text">Ce court billet présente un aperçu des enjeux actuels en communication santé. Nous y abordons les relations avec les médias, la gestion des parties prenantes et les stratégies d'affaires publiques qui soutiennent les organisations du réseau de la santé au quotidien.</p>
    <p class="post-text">Découvrez nos recommandations pratiques, des exemples concrets tirés de nos mandats récents et quelques pistes de réflexion pour mieux planifier vos prochaines prises de parole publiques.</p>
  </div>
  <div class="btn-read">Article complet <svg width="22" height="22" viewBox="0 0 22 22"><rect width="22" height="22" fill="#333"/><path d="M8 5l6 6-6 6" stroke="#f7d21a" stroke-width="3" fill="none"/></svg></div>
</article>

<article class="post" style="top:1320px">
  <div class="post-image" role="img" aria-label="Photo d'un coucher de soleil sur la mer" style="background:linear-gradient(180deg,#f6b24a,#e2632a 50%,#7a2f1e)"></div>
  <div class="post-body">
    <h3 class="post-title">Titre de la publication</h3>
    <p class="post-date">23 juillet 2013</p>
    <p class="post-text">Ce court billet présente un aperçu des enjeux actuels en communication santé. Nous y abordons les relations avec les médias, la gestion des parties prenantes et les stratégies d'affaires publiques qui soutiennent les organisations du réseau de la santé au quotidien.</p>
    <p class="post-text">Découvrez nos recommandations pratiques, des exemples concrets tirés de nos mandats récents et quelques pistes de réflexion pour mieux planifier vos prochaines prises de parole publiques.</p>
  </div>
  <div class="btn-read">Article complet <svg width="22" height="22" viewBox="0 0 22 22"><rect width="22" height="22" fill="#333"/><path d="M8 5l6 6-6 6" stroke="#f7d21a" stroke-width="3" fill="none"/></svg></div>
</article>

<article class="post" style="top:1680px">
  <div class="post-image" role="img" aria-label="Photo d'une rizière en terrasses verdoyante" style="background:linear-gradient(170deg,#cfdcc0,#86a85a 45%,#4f7a34)"></div>
  <div class="post-body">
    <h3 class="post-title">Titre de la publication</h3>
    <p class="post-date">23 juillet 2013</p>
    <p class="post-text">Ce court billet présente un aperçu des enjeux actuels en communication santé. Nous y abordons les relations avec les médias, la gestion des parties prenantes et les stratégies d'affaires publiques qui soutiennent les organisations du réseau de la santé au quotidien.</p>
    <p class="post-text">Découvrez nos recommandations pratiques, des exemples concrets tirés de nos mandats récents et quelques pistes de réflexion pour mieux planifier vos prochaines prises de parole publiques.</p>
  </div>
  <div class="btn-read">Article complet <svg width="22" height="22" viewBox="0 0 22 22"><rect width="22" height="22" fill="#333"/><path d="M8 5l6 6-6 6" stroke="#f7d21a" stroke-width="3" fill="none"/></svg></div>
</article>

<footer class="site-footer">
  <div class="feed-name">Chirpline</div>
  <ul class="tweets">
    <li>Nouvelle analyse sur la réforme du financement des hôpitaux, à lire sur notre blogue #santé <span class="handle">@SoleneVerbruggen</span></li>
    <li>Merci à toute l'équipe pour le colloque d'hier, une belle journée d'échanges <span class="handle">@SoleneVerbruggen</span></li>
    <li>Nos conseils pour bien préparer une entrevue médiatique en contexte de crise <span class="handle">@SoleneVerbruggen</span></li>
  </ul>
  <div class="btn-follow">Suivre @SoleneVerbruggen</div>
  <div class="newsletter">
    <h3>Recevez nos publications</h3>
    <div class="field"><label>Votre nom:</label><span></span></div>
    <div class="field"><label>Votre courriel:</label><span></span></div>
    <div class="btn-subscribe">Abonnez-vous</div>
  </div>
  <div class="legal">© Solène Verbruggen · Tous droits réservés</div>
</footer>

</body>
</html>
```